Poster for IT remote support company

We need two A1 posters for a trade show. We offer IT remote support to businesses - please see www.qorlimbe.co.uk for further info., but do not use our web site design as a baseline as we do not like it that much!

We would like to communicate that we can provide everything a business needs related to their IT under one roof, solve all their IT worries, and speak their language rather than IT jargon.

I would like them to look quite modern and stylish, with something that is eye catching rather than too wordy. Although as a pair one poster could have more text, or they could focus on two different things we do??

We did come up with a few ideas around it being time to sort out your IT, getting IT to run like clockwork, getting rid of IT related stress...but could not make it look 'pretty' on a poster!

Over to you...
Updates

Should have said that our existing marketing materials use the blue colour in our logo and sometimws a lime green colour.

We do have a strapline for the logo - For all yout IT needs.

Target Market(s)

Smallish business owners who have 5-50 PCs but not in house IT staff

Industry/Entity Type

Business

Requirements
Must have
• A set of two posters with bold text that is eye catching
• A call us now bit
Should not have
• Too many words
• Logo as the title headline

```html
<!DOCTYPE html>
<html lang="en">
<head>
<meta charset="utf-8">
<title>Brightvane – Trade Show Posters</title>
<link rel="stylesheet" href="https://fonts.googleapis.com/css2?family=Archivo:wght@700;800;900&display=swap">
<style>
  :root {
    --stage: #0d1420;
    --navy: #14233d;
    --blue-deep: #0b3f73;
    --blue-mid: #1a6fb0;
    --blue-light: #5cc3ee;
    --ice: #dff1fb;
    --white: #ffffff;
    --bar-grey: #3b4046;
    --steel: #4d8fb5;
    --badge: #1b1d20;
  }
  * { box-sizing: border-box; margin: 0; padding: 0; }
  html, body {
    width: 1200px; height: 928px; overflow: hidden;
    background: var(--stage);
    font-family: "Archivo", "Helvetica Neue", Arial, sans-serif;
  }
  .canvas { position: relative; width: 1200px; height: 928px; }

  .poster {
    position: absolute; overflow: hidden; background: var(--white);
    box-shadow: 0 10px 40px rgba(0,0,0,.5);
  }
  .poster--vertical { left: 70px; top: 144px; width: 440px; height: 640px; }
  .poster--horizontal { left: 550px; top: 244px; width: 590px; height: 440px; }

  .poster__image {
    position: absolute; inset: 0;
    background:
      radial-gradient(ellipse at 70% 45%, rgba(223,241,251,.85) 0%, rgba(92,195,238,.35) 22%, transparent 50%),
      linear-gradient(160deg, var(--blue-mid) 0%, var(--blue-deep) 55%, #082a4f 100%);
  }
  .poster__top-curve, .poster__bottom-curve { position: absolute; left: 0; width: 100%; }
  .poster__top-curve { top: 0; }
  .poster__bottom-curve { bottom: 0; }

  .brand {
    position: absolute; display: flex; align-items: center; gap: 6px;
    color: var(--navy); font-weight: 700; font-size: 26px; letter-spacing: -.5px;
  }
  .brand__dot { width: 9px; height: 9px; border-radius: 50%; background: var(--blue-mid); }
  .poster--vertical .brand { left: 26px; top: 22px; }
  .poster--horizontal .brand { right: 30px; top: 22px; }

  .headline {
    position: absolute; color: var(--white); font-weight: 900;
    text-transform: uppercase; letter-spacing: -2px;
  }
  .poster--vertical .headline {
    left: 24px; top: 96px; font-size: 66px; line-height: .86;
  }

  .badge {
    position: absolute; border-radius: 50%; background: var(--badge);
    display: flex; flex-direction: column; justify-content: center;
    color: var(--white); font-weight: 800; text-transform: uppercase;
  }
  .badge__lead { color: var(--blue-light); }
  .poster--vertical .badge {
    left: 290px; top: 300px; width: 130px; height: 130px;
    padding-left: 18px; font-size: 15px; line-height: 1;
  }
  .poster--horizontal .badge {
    left: 452px; top: 280px; width: 110px; height: 110px;
    padding-left: 16px; font-size: 13px; line-height: 1;
  }

  .contact-bar {
    position: absolute; left: 96px; top: 556px; width: 320px; height: 30px;
    background: var(--bar-grey); color: var(--blue-light);
    font-weight: 700; font-size: 9.5px; letter-spacing: .5px;
    padding: 4px 0 0 26px; line-height: 1.25;
  }
  .contact-bar__web { letter-spacing: 4px; }
  .contact-bar__disc {
    position: absolute; left: 56px; top: 540px; width: 56px; height: 56px;
    border-radius: 50%; background: var(--steel);
  }
  .contact-bar__accent {
    position: absolute; left: 300px; top: 590px; width: 116px; height: 6px;
    background: var(--blue-mid);
  }

  .tagline {
    position: absolute; left: 0; width: 100%; text-align: center;
    color: var(--white); font-weight: 800; letter-spacing: -1px;
  }
  .tagline--main { top: 112px; font-size: 44px; line-height: 1.05; }
  .tagline--reflection {
    top: 214px; font-size: 44px; line-height: 1; transform: scaleY(-1);
    opacity: .18;
  }
  .poster--horizontal .contact {
    position: absolute; left: 36px; top: 330px;
    color: var(--white); font-weight: 700; font-size: 9.5px; line-height: 1.35;
  }
  .poster--horizontal .contact__web { letter-spacing: 4px; }
  .tech-strip {
    position: absolute; left: 0; bottom: 0; width: 100%; height: 34px;
    background: linear-gradient(180deg, var(--ice) 0%, var(--blue-light) 45%, var(--blue-deep) 100%);
  }
</style>
</head>
<body>
<main class="canvas">

  <section class="poster poster--vertical" aria-label="Vertical poster: time to sort out your IT">
    <div class="poster__image" role="img" aria-label="Blue glass and clock photograph with light flare"></div>
    <svg class="poster__top-curve" width="440" height="90" viewBox="0 0 440 90" aria-hidden="true">
      <path d="M0 0H440V52C300 70 150 74 0 84Z" fill="var(--white)"/>
    </svg>
    <svg class="poster__bottom-curve" width="440" height="130" viewBox="0 0 440 130" aria-hidden="true">
      <path d="M0 40C150 6 300 0 440 4V130H0Z" fill="var(--white)"/>
    </svg>
    <div class="brand"><span class="brand__name">Brightvane</span><span class="brand__dot"></span></div>
    <h1 class="headline">Time<br>to<br>sort<br>out<br>your<br>IT</h1>
    <div class="badge"><span class="badge__lead">All your</span><span>IT needs</span><span>under</span><span>one roof</span></div>
    <div class="contact-bar__disc"></div>
    <div class="contact-bar">
      <div>Telephone number : 01632 960418</div>
      <div class="contact-bar__web">www.qorlimbe.co.uk</div>
    </div>
    <div class="contact-bar__accent"></div>
  </section>

  <section class="poster poster--horizontal" aria-label="Horizontal poster: getting IT to run like clockwork">
    <div class="poster__image" role="img" aria-label="Blue photograph of a clock face behind glass"></div>
    <svg class="poster__top-curve" width="590" height="80" viewBox="0 0 590 80" aria-hidden="true">
      <path d="M0 0H590V62C400 50 200 48 0 56Z" fill="var(--white)"/>
    </svg>
    <div class="brand"><span class="brand__name">Brightvane</span><span class="brand__dot"></span></div>
    <h1 class="tagline tagline--main">getting IT to run<br>like clockwork</h1>
    <div class="tagline tagline--reflection" aria-hidden="true">like clockwork</div>
    <div class="badge"><span class="badge__lead">All your</span><span>IT needs</span><span>under</span><span>one roof</span></div>
    <div class="contact">
      <div>Telephone number : 01632 960418</div>
      <div class="contact__web">www.qorlimbe.co.uk</div>
    </div>
    <div class="tech-strip" role="img" aria-label="Glowing blue technology light streaks"></div>
  </section>

</main>
</body>
</html>
```